Quillory Nest Business Card

I need a business card design. We are a collaborate online training company. Our colors are gray and green. Our website is QuilloryNest.com

I would like an area for a profile picture within the card

```html
<!DOCTYPE html>
<html lang="en">
<head>
<meta charset="utf-8">
<title>Quillory Nest Business Card</title>
<link href="https://fonts.googleapis.com/css2?family=Montserrat:wght@400;500;700;800&display=swap" rel="stylesheet">
<style>
  :root {
    --bg: #2b2b2b;
    --card: #050505;
    --green: #8dc63f;
    --white: #ffffff;
    --photo-top: #4a4a4a;
    --photo-bottom: #1c1c1c;
  }
  * { box-sizing: border-box; margin: 0; padding: 0; }
  html, body { width: 1200px; height: 900px; overflow: hidden; }
  body {
    background: var(--bg);
    font-family: 'Montserrat', sans-serif;
    color: var(--white);
    position: relative;
  }
  .card {
    position: absolute;
    width: 720px;
    height: 410px;
    background: var(--card);
    border-radius: 22px;
    overflow: hidden;
    box-shadow: 0 14px 30px rgba(0,0,0,.45);
  }
  .card--front { left: 120px; top: 25px; }
  .card--back { left: 360px; top: 465px; }
  .card__bands { position: absolute; inset: 0; width: 720px; height: 410px; }

  .profile-photo {
    position: absolute;
    left: 120px; top: 50px;
    width: 250px; height: 332px;
    background: linear-gradient(180deg, var(--photo-top), var(--photo-bottom));
    border-radius: 6px 6px 0 0;
  }

  .brand { position: absolute; display: flex; align-items: center; gap: 12px; }
  .brand__dot { width: 46px; height: 46px; border-radius: 50%; background: var(--green); flex: none; }
  .brand__name { font-weight: 800; font-size: 40px; letter-spacing: -1.5px; color: var(--white); white-space: nowrap; }
  .card--front .brand { right: 40px; top: 110px; gap: 10px; }
  .card--front .brand__dot { width: 40px; height: 40px; }
  .card--front .brand__name { font-size: 34px; letter-spacing: -1.2px; }
  .card--back .brand { left: 40px; top: 60px; }

  .front__web { position: absolute; right: 40px; top: 180px; font-size: 17px; }

  .holder { position: absolute; right: 40px; top: 140px; text-align: right; }
  .holder__name { font-weight: 800; font-size: 30px; color: var(--green); letter-spacing: .5px; line-height: 1; }
  .holder__role { font-weight: 500; font-size: 15px; letter-spacing: 1px; margin-top: 2px; }
  .divider { position: absolute; left: 40px; right: 40px; top: 205px; height: 2px; background: var(--green); }
  .address { position: absolute; right: 40px; top: 220px; text-align: right; font-size: 15px; line-height: 1.45; }

  .contacts { position: absolute; left: 40px; top: 222px; list-style: none; font-size: 16px; line-height: 1.55; }
  .contacts li { display: flex; align-items: center; gap: 12px; }
  .contacts svg { width: 14px; height: 14px; flex: none; }
</style>
</head>
<body>

<section class="card card--front">
  <div class="profile-photo" role="img" aria-label="Profile photograph of the founder"></div>
  <div class="brand">
    <span class="brand__dot"></span>
    <span class="brand__name">QuilloryNest</span>
  </div>
  <p class="front__web">www.quillorynest.com</p>
  <svg class="card__bands" viewBox="0 0 720 410" aria-hidden="true">
    <polygon points="0,382 470,382 455,410 0,410" fill="var(--green)"/>
    <polygon points="484,355 720,355 720,380 470,380" fill="var(--white)"/>
  </svg>
</section>

<section class="card card--back">
  <div class="brand">
    <span class="brand__dot"></span>
    <span class="brand__name">QuilloryNest</span>
  </div>
  <div class="holder">
    <p class="holder__name">DALEN MARSH</p>
    <p class="holder__role">FOUNDER</p>
  </div>
  <div class="divider"></div>
  <p class="address">2480 W Harlow Ave. Suite 7<br>Marlowe, Arizona 85299</p>
  <ul class="contacts">
    <li>
      <svg viewBox="0 0 16 16" aria-hidden="true"><path d="M3 1l3 3-1.5 2a9 9 0 0 0 5.5 5.5L12 10l3 3-2 2C7 15 1 9 1 3z" fill="var(--green)"/></svg>
      (302) 555-0147
    </li>
    <li>
      <svg viewBox="0 0 16 16" aria-hidden="true"><rect x="1" y="3" width="14" height="10" fill="none" stroke="var(--green)" stroke-width="1.6"/><path d="M1 3l7 6 7-6" fill="none" stroke="var(--green)" stroke-width="1.6"/></svg>
      info@quillorynest.com
    </li>
    <li>
      <svg viewBox="0 0 16 16" aria-hidden="true"><circle cx="8" cy="8" r="6.5" fill="none" stroke="var(--green)" stroke-width="1.6"/><path d="M1.5 8h13M8 1.5c-3 3.5-3 9.5 0 13M8 1.5c3 3.5 3 9.5 0 13" fill="none" stroke="var(--green)" stroke-width="1.2"/></svg>
      www.quillorynest.com
    </li>
  </ul>
  <svg class="card__bands" viewBox="0 0 720 410" aria-hidden="true">
    <polygon points="0,382 560,382 545,410 0,410" fill="var(--green)"/>
    <polygon points="574,355 720,355 720,380 560,380" fill="var(--white)"/>
  </svg>
</section>

</body>
</html>
```